Denim Retailer needs advert for sale

We need a advertisement designed that can be used to market our upcoming promotion through our electronic media channels which include Facebook, email & website.

Promotion Details:

Title: Pick A Pair Sale
Offer: Buy 1 pair =10% off, Buy 2 pairs = 15% off, Buy 3+ pairs = 20% off.

Our main brands are Tavon's, Gallop by Orn & Cobbleton for both men and women.

Our Target market is 25-55 yo male & female.

I would ideally like an eye catching design that encapsulates premise of our promotion. I don't have any specific theme or colour scheme, bust must be gender neutral.

Target Market(s)

25-55 male & female

Industry/Entity Type

Electronic

Requirements
Must have
• Must be sized to accommodate a Facebook post.

```html
<!DOCTYPE html>
<html lang="en">
<head>
<meta charset="utf-8">
<title>Pick A Pair Sale</title>
<link rel="stylesheet" href="https://fonts.googleapis.com/css2?family=Roboto+Condensed:wght@700&display=swap">
<style>
  :root {
    --backdrop: #e6e8ec;
    --card: #fbfbf9;
    --red: #d0202a;
    --ink: #111111;
  }
  * { margin: 0; padding: 0; box-sizing: border-box; }
  html, body {
    width: 1200px;
    height: 864px;
    overflow: hidden;
    background: var(--backdrop);
  }
  .sale-card {
    position: absolute;
    left: 80px;
    top: 92px;
    width: 1040px;
    height: 680px;
    background: var(--card);
    box-shadow: 0 6px 24px rgba(0, 0, 0, 0.12);
    font-family: "Roboto Condensed", "Arial Narrow", sans-serif;
    font-weight: 700;
  }
  .step-number {
    position: absolute;
    top: 20px;
    font-size: 230px;
    line-height: 1;
    color: var(--red);
  }
  .step-one { left: 70px; }
  .step-two { left: 420px; }
  .step-three { left: 790px; }
  .step-divider {
    position: absolute;
    top: 70px;
    width: 10px;
    height: 160px;
    background: repeating-linear-gradient(to bottom, var(--ink) 0 10px, transparent 10px 20px);
  }
  .divider-a { left: 340px; }
  .divider-b { left: 700px; }
  .offer-list {
    position: absolute;
    left: 64px;
    top: 272px;
    list-style: none;
    color: var(--red);
    font-size: 31px;
    line-height: 1.12;
    text-transform: uppercase;
  }
  .brand-note {
    position: absolute;
    left: 420px;
    top: 300px;
    color: var(--ink);
    font-size: 29px;
    line-height: 1.15;
    text-transform: uppercase;
  }
  .brand-note .audience { color: var(--red); }
  .sale-title {
    position: absolute;
    left: 60px;
    bottom: 50px;
    color: var(--ink);
    font-size: 132px;
    line-height: 1;
    letter-spacing: -1px;
    text-transform: uppercase;
  }
</style>
</head>
<body>
  <main class="sale-card">
    <span class="step-number step-one">1</span>
    <span class="step-divider divider-a"></span>
    <span class="step-number step-two">2</span>
    <span class="step-divider divider-b"></span>
    <span class="step-number step-three">3</span>

    <ul class="offer-list">
      <li>Buy 1 pair = 10% off</li>
      <li>Buy 2 pairs = 15% off</li>
      <li>Buy 3+ pairs = 20% off</li>
    </ul>

    <p class="brand-note">
      Main brands include Tavon's,<br>
      Gallop by Orn &amp; Cobbleton<br>
      <span class="audience">For both men and women</span>
    </p>

    <h1 class="sale-title">Pick A Pair Sale</h1>
  </main>
</body>
</html>
```